WordPress design project for Brindlow Construction

Brindlow Construction, Inc. (www.brindlowinc.example) is a private organization. It is run by the same family that founded Brindlow Waste Systems (www.brindlow.example), a large, publicly-held waste management organization in the US. While owned by the same family, the two organizations are run independently.
Brindlow Construction is a well-established New England USA construction outfit specializing in site development, heavy excavation, aggregate, large-scale/municipal water and sewer systems, and landfill construction and closure. Brindlow Construction is not in any way a residential or commercial building contractor.
Brindlow Construction also operates hydraulic and hydrostatic service shops, as well as aggregate (gravel, sand, stone, top soil, and anything else aggregate) sites. Both are for more traditional, non-project customers, such as landscapers and other construction companies.
Business contact information is as noted below:
Address:
Brindlow Construction, Inc.
48 Quarry Row
Fairhollow, Vermont 05799
Telephone:
802-555-0148
Fax:
802-555-0193
Email:
info@brindlowinc.example
A tagline used in a recent advertisement was:
"Committed to providing a complete array of services for over 30 years, we are New England's premier construction company."
In reviewing design ideas internally, we found bits and pieces of the following sites appealing:
TR Construction (Wendermoor) - http://www.trconstruction.example/
Halvorsk Construction - http://www.halvorsk.example/
Pellow Construction - http://www.pellowconstruction.example/
Greyfield Construction Group - http://www.greyfieldconstructiongroup.example/
Varko Construction - http://www.varko.example/
Lindqvist Brothers Construction http://www.lindqvistbros.example/
Ormsby Construction http://www.ormsby-corp.example/
The blue in the logo is hex #00253f. The logo was designed by hand many years ago, so the font is unknown.
We would like a fresh, professional design that effectively illustrates what we do in a thoughtful, impressive way.
Target Market(s)
Would-be clients, land developers, waste organizations, energy developers, engineers, surveyors, landscapers, heavy equipment operators and the likes.
Industry/Entity Type
Waste Management
Requirements
Must have
- Lots of media capabilities, such as embedded video (via YouTube is fine), project image gallery, and sliders for various functions.
A large slider on the landing page is critical, as well as space for standard things, such as news/events, job opportunities, project highlights, and the likes.
We also want to highlight things like employee longevity. Some of our team have been with us since the beginning.
We need to add emphasis to the fact that our hydraulic/hydro static services and aggregate operations are for anyone who needs such service or material. Related, we need a place to set prices and descriptions of such material to help site visitors decide what they may need.
We need a place to highlight business partners, such as Felix Harrow and Ironbeetle.
We also need form capabilities for things like bid requests and general contacts from the public. Related, there should be social media capabilities.
Nice to have
- This is almost a must have, but we're open to options. The WordPress design should be capable of fitting into the very popular PlyFrames Trellis theme.

```html
<!DOCTYPE html>
<html lang="en">
<head>
<meta charset="utf-8">
<title>Brindlow Construction — Home</title>
<link href="https://fonts.googleapis.com/css2?family=Open+Sans:ital,wght@0,300;0,400;0,600;1,400&family=Roboto:wght@400;500;700&display=swap" rel="stylesheet">
<style>
:root{
  --navy:#00253f;
  --blue:#0f4a8a;
  --ink:#333a40;
  --muted:#8a8f94;
  --rule:#dedede;
  --page:#f4f4f4;
  --panel:#ffffff;
  --dark:#2b2b2b;
}
*{box-sizing:border-box;margin:0;padding:0}
html,body{width:705px;height:1200px;overflow:hidden}
body{position:relative;background:var(--page);font-family:"Open Sans",Arial,sans-serif;color:var(--ink)}
.abs{position:absolute}
.topbar{left:0;top:0;width:705px;height:3px;background:#111}
.topbar-active{left:270px;top:0;width:60px;height:3px;background:#d6d6d6}
.search{left:510px;top:3px;width:121px;height:13px;background:#fff;border:1px solid #d8d8d8;border-top:none;font-size:6px;color:#b5b5b5;padding:2px 5px;font-style:italic}
.logo{left:66px;top:22px;width:123px;height:32px;display:flex;align-items:center;gap:6px}
.logo-mark{width:12px;height:12px;background:var(--navy)}
.logo-name{font-family:Roboto,sans-serif;font-weight:700;color:var(--navy);font-size:12px;line-height:1.05}
.nav{top:33px;font-family:Roboto,sans-serif}
.nav b{display:block;font-size:7.2px;font-weight:500;color:#222;letter-spacing:.1px}
.nav i{display:block;font-family:"Open Sans",sans-serif;font-size:5.6px;color:#999;margin-top:2px}
.nav.active b{color:var(--blue)}
.nav-underline{left:274px;top:64px;width:61px;height:1px;background:var(--navy)}
.nav-pointer{left:301px;top:64px}
.rule{height:1px;background:var(--rule)}
.quote{left:0;width:705px;top:92px;text-align:center;font-weight:300;font-size:14px;line-height:19px;color:#555}
.slider{left:61px;top:156px;width:575px;height:221px;border-radius:4px 4px 0 0;background:linear-gradient(100deg,#3a3a36 0%,#6d6a5c 30%,#c9c4b0 55%,#e6e3d8 75%,#d2d4cc 100%)}
.slide-caption{left:78px;top:216px;width:232px;height:90px;background:rgba(230,230,232,.88);border-radius:2px;font-family:Roboto,sans-serif;color:var(--navy);padding:8px 0 0 9px}
.slide-caption .big{font-size:41px;font-weight:500;line-height:42px;letter-spacing:-.5px}
.slide-caption .small{font-size:26px;font-weight:500;line-height:30px;padding-left:8px}
.dots{left:88px;top:360px;display:flex;gap:2px}
.dots span{width:4px;height:4px;border-radius:50%;background:#fff}
.services{left:61px;top:379px;width:575px;height:48px;background:#fafafa;border-bottom:1px solid #d5d5d5;display:flex}
.service{flex:1;display:flex;align-items:center;gap:6px;padding-left:9px;border-right:1px solid #e6e6e6}
.service.current{background:#e9e9e9;border-right:none}
.service svg{flex:none}
.service b{display:block;font-family:Roboto,sans-serif;font-weight:400;font-size:8.8px;color:#333}
.service.current b{color:var(--blue)}
.service span{display:block;font-size:6.2px;color:#999}
.services-shadow{left:430px;top:427px;width:206px;height:12px;background:radial-gradient(ellipse at 70% 0%,rgba(0,0,0,.18),rgba(0,0,0,0) 70%)}
h2{position:absolute;font-family:Roboto,sans-serif;font-weight:400;font-size:13px;color:#222}
.arrow{position:absolute;width:11px;height:11px;border-radius:50%;background:#3c3c3c}
.arrow.next{background:var(--blue)}
.arrow svg{display:block}
.project-img{top:489px;height:105px}
.project-title{top:601px;font-family:Roboto,sans-serif;font-size:9px;color:#222}
.project-text{top:620px;width:178px;font-size:7px;line-height:10px;color:#999}
.news-title{left:82px;font-size:7px;color:#777}
.news-title a{color:var(--blue);text-decoration:none}
.news-date{left:83px;font-size:7px;font-style:italic;color:var(--blue)}
.news-text{left:83px;width:220px;font-size:7px;line-height:11px;color:#777}
.read-more{left:350px;width:37px;text-align:right;font-size:6.8px;color:#888}
.team{left:414px;width:71px;height:70px;border:1px solid #ddd;background:linear-gradient(180deg,#dfe4ea,#a9b2bd 60%,#3c4350)}
.box{left:76px;top:916px;width:555px;height:182px;background:var(--panel);border:1px solid #e2e2e2}
h3{position:absolute;font-family:Roboto,sans-serif;font-weight:400;font-size:12px;color:var(--blue);display:flex;align-items:center;gap:8px}
h3::after{content:"";display:block;height:1px;background:#d8d8d8}
.h3-contact::after{width:56px}
.h3-clients::after{width:66px}
.h3-video::after{width:84px}
.field{left:89px;width:143px;border:1px solid #ccc;background:#fff;font-size:6.5px;color:var(--navy);padding:3px 5px}
.submit{left:89px;top:1066px;width:69px;height:19px;background:var(--navy);color:#fff;font-family:Roboto,sans-serif;font-size:9px;font-weight:500;text-align:center;line-height:19px;border-radius:2px}
.client{font-family:Roboto,sans-serif;font-weight:700;color:#4a4f55;font-size:11px}
.video{left:446px;top:948px;width:176px;height:102px;background:linear-gradient(160deg,#6f6a5e,#c2c7cc 45%,#9aa6b2 70%,#5d6874)}
.video-bar{left:446px;top:1038px;width:176px;height:12px;background:#1b1b1b;font-size:4.5px;color:#bbb}
.video-caption{left:446px;top:1050px;width:176px;height:38px;background:#eeeeee;font-size:6.6px;line-height:9px;color:#999;padding:15px 6px 0}
.social{left:78px;top:1114px;width:548px;height:31px;background:#fff;border:1px solid #e6e6e6;display:flex;align-items:center}
.social-item{flex:1;display:flex;align-items:center;gap:6px;padding-left:8px;border-right:1px solid #e8e8e8;height:20px}
.social-item:last-child{border-right:none}
.social-item i{width:16px;height:16px;background:#c9cdd2;flex:none}
.social-item small{display:block;font-size:5.4px;color:#aaa}
.social-item b{display:block;font-family:Roboto,sans-serif;font-weight:500;font-size:8px;color:#222}
.footer{left:0;top:1166px;width:705px;height:34px;background:var(--dark);font-size:6.3px;color:#bbb}
.footer-links{position:absolute;left:67px;top:14px;word-spacing:1px}
.footer-copy{position:absolute;left:513px;top:14px}
</style>
</head>
<body>
<div class="abs topbar"></div>
<div class="abs topbar-active"></div>
<div class="abs search">Search</div>

<div class="abs logo"><span class="logo-mark"></span><span class="logo-name">Brindlow<br>Construction Inc</span></div>

<div class="abs nav active" style="left:287px"><b>HOME</b><i>starts here</i></div>
<div class="abs nav" style="left:332px"><b>WHO WE ARE</b><i>about company</i></div>
<div class="abs nav" style="left:400px"><b>WHAT WE DO</b><i>what we think</i></div>
<div class="abs nav" style="left:469px"><b>WHERE WE ARE</b><i>abput place</i></div>
<div class="abs nav" style="left:543px"><b>NEWS</b><i>update</i></div>
<div class="abs nav" style="left:586px"><b>ABOUT US</b><i>know about us</i></div>
<div class="abs nav-underline"></div>
<svg class="abs nav-pointer" width="6" height="4" viewBox="0 0 6 4"><path d="M0 0h6L3 3z" fill="#00253f"/></svg>
<div class="abs rule" style="left:61px;top:66px;width:575px"></div>

<p class="abs quote">"Committed to providing a complete array of services for over 30 years, we are<br>New England's premier construction company."</p>

<div class="abs slider" role="img" aria-label="Engineers in hard hats reviewing plans on site"></div>
<div class="abs slide-caption"><div class="big">Technology</div><div class="small">working for you</div></div>
<div class="abs dots"><span></span><span></span><span></span></div>

<div class="abs services">
  <div class="service"><svg width="22" height="22" viewBox="0 0 22 22"><circle cx="11" cy="11" r="10" fill="#3a3a3a"/><rect x="6" y="9" width="10" height="5" rx="1" fill="#fff"/><circle cx="8" cy="15" r="1.5" fill="#fff"/><circle cx="14" cy="15" r="1.5" fill="#fff"/></svg><div><b>Heavy Excavation</b><span>Lorem Ipsum is simply</span></div></div>
  <div class="service"><svg width="22" height="22" viewBox="0 0 22 22"><circle cx="11" cy="11" r="10" fill="#3a3a3a"/><circle cx="11" cy="11" r="5" fill="none" stroke="#fff" stroke-width="2" stroke-dasharray="2 1.2"/><circle cx="11" cy="11" r="1.8" fill="#fff"/></svg><div><b>Sewer Systems</b><span>Lorem Ipsum is simply</span></div></div>
  <div class="service"><svg width="22" height="22" viewBox="0 0 22 22"><circle cx="11" cy="11" r="10" fill="#3a3a3a"/><rect x="7" y="6" width="8" height="1.5" fill="#fff"/><path d="M7.5 8.5h7l-.8 8h-5.4z" fill="#fff"/></svg><div><b>Waste System</b><span>Lorem Ipsum is simply</span></div></div>
  <div class="service current"><svg width="22" height="22" viewBox="0 0 22 22"><circle cx="11" cy="11" r="10" fill="#3a3a3a"/><path d="M6 16l6-6M11 7l4 4" stroke="#fff" stroke-width="2"/></svg><div><b>Aggregate</b><span>Lorem Ipsum is simply</span></div></div>
</div>
<div class="abs services-shadow"></div>
<div class="abs rule" style="left:82px;top:449px;width:550px"></div>

<h2 style="left:82px;top:467px">Recent projects</h2>
<span class="arrow" style="left:599px;top:464px"><svg width="11" height="11" viewBox="0 0 11 11"><path d="M6.5 3L4 5.5 6.5 8" stroke="#fff" fill="none"/></svg></span>
<span class="arrow next" style="left:617px;top:464px"><svg width="11" height="11" viewBox="0 0 11 11"><path d="M4.5 3L7 5.5 4.5 8" stroke="#fff" fill="none"/></svg></span>

<div class="abs project-img" style="left:82px;width:178px;background:linear-gradient(135deg,#f4f4f4,#c8c8c8 60%,#8a8a8a)" role="img" aria-label="Compass close-up pointing to opportunities"></div>
<div class="abs project-img" style="left:271px;width:177px;background:radial-gradient(circle at 55% 60%,#d9c25a 0,#4a4e5c 30%,#262a36 80%)" role="img" aria-label="Glowing exclamation mark among question marks"></div>
<div class="abs project-img" style="left:458px;width:173px;background:linear-gradient(150deg,#8fb4d8,#dfe9f3 55%,#a7bcd3)" role="img" aria-label="Hands reviewing printed charts with a pen"></div>

<div class="abs project-title" style="left:82px">The Opportunity</div>
<div class="abs project-title" style="left:273px">The Solution</div>
<div class="abs project-title" style="left:461px">The Results</div>
<p class="abs project-text" style="left:83px">Lorem Ipsum is simply dummy text of the printing and typesetting industry. Lorem Ipsum has been the industry's standard dummy text ever since the 1500s, when an unknown printer took a galley of type and scrambled it to make.</p>
<p class="abs project-text" style="left:273px">Lorem Ipsum is simply dummy text of the printing and typesetting industry. Lorem Ipsum has been the industry's standard dummy text ever since the 1500s, when an unknown printer took a galley of type and scrambled it to make.</p>
<p class="abs project-text" style="left:459px">Lorem Ipsum is simply dummy text of the printing and typesetting industry. Lorem Ipsum has been the industry's standard dummy text ever since the 1500s, when an unknown printer took a galley of type and scrambled it to make.</p>
<div class="abs rule" style="left:82px;top:693px;width:510px"></div>

<h2 style="left:82px;top:712px">Latest News</h2>
<h2 style="left:415px;top:712px">Our Team</h2>
<span class="arrow" style="left:599px;top:715px"><svg width="11" height="11" viewBox="0 0 11 11"><path d="M6.5 3L4 5.5 6.5 8" stroke="#fff" fill="none"/></svg></span>
<span class="arrow next" style="left:617px;top:715px"><svg width="11" height="11" viewBox="0 0 11 11"><path d="M4.5 3L7 5.5 4.5 8" stroke="#fff" fill="none"/></svg></span>

<div class="abs news-title" style="top:738px">Elric Downs Wairau Sauvignon Blanc –<a>Summer in a Bottle</a></div>
<div class="abs news-date" style="top:749px">posted on March 13, 2013 20:15</div>
<p class="abs news-text" style="top:766px">Media release; summer has never tasted better than with Elric Downs' 2012 Sauvignon Blanc</p>
<div class="abs read-more" style="top:790px">Read More</div>
<div class="abs rule" style="left:82px;top:801px;width:305px"></div>

<div class="abs news-title" style="top:817px">Torvale Barbecue a winner for Auckland Mum</div>
<div class="abs news-date" style="top:828px">posted on March 13, 2013 20:15</div>
<p class="abs news-text" style="top:848px;left:81px">Media release; A new barbecue at home and a trip for two to Queenstown, Mara Tolley all set after winning with Torvale</p>
<div class="abs read-more" style="top:873px">Read More</div>

<div class="abs team" style="top:738px" role="img" aria-label="Team member portrait"></div>
<div class="abs team" style="left:488px;top:738px" role="img" aria-label="Team member portrait"></div>
<div class="abs team" style="left:562px;top:738px" role="img" aria-label="Team member portrait"></div>
<div class="abs team" style="top:811px" role="img" aria-label="Team member portrait"></div>
<div class="abs team" style="left:488px;top:811px" role="img" aria-label="Team member portrait"></div>
<div class="abs team" style="left:562px;top:811px" role="img" aria-label="Team member portrait"></div>
<div class="abs rule" style="left:82px;top:902px;width:510px"></div>

<div class="abs box"></div>
<h3 class="h3-contact" style="left:88px;top:928px">Contact Form</h3>
<h3 class="h3-clients" style="left:269px;top:928px">Our Clients</h3>
<h3 class="h3-video" style="left:447px;top:928px">Featured Video</h3>

<div class="abs field" style="top:953px;height:17px">Name:</div>
<div class="abs field" style="top:978px;height:17px">Email:</div>
<div class="abs field" style="top:1003px;height:56px">Message</div>
<div class="abs submit">Submit</div>

<div class="abs client" style="left:260px;top:990px">Felix Harrow</div>
<div class="abs client" style="left:330px;top:993px">Ironbeetle</div>
<div class="abs client" style="left:264px;top:1037px">Softwave</div>
<div class="abs client" style="left:339px;top:1034px">Bleepo</div>

<div class="abs video" role="img" aria-label="Hands working over construction blueprints"></div>
<svg class="abs" style="left:520px;top:982px" width="26" height="26" viewBox="0 0 26 26"><circle cx="13" cy="13" r="13" fill="#111"/><path d="M10 8l9 5-9 5z" fill="#fff"/></svg>
<div class="abs video-bar">
  <svg class="abs" style="left:8px;top:3px" width="60" height="6" viewBox="0 0 60 6"><rect x="0" y="0" width="1.5" height="6" fill="#ddd"/><rect x="3" y="0" width="1.5" height="6" fill="#ddd"/><path d="M20 2h2l2-2v6l-2-2h-2z" fill="#ddd"/><rect x="36" y="2" width="20" height="2" fill="#c0202a"/><rect x="56" y="0" width="2" height="6" fill="#ddd"/></svg>
  <span class="abs" style="left:69px;top:3px">06:24 / 09:35</span>
  <span class="abs" style="left:153px;top:3px">360p</span>
</div>
<div class="abs rule" style="left:446px;top:1036px;width:176px;background:#888"></div>
<p class="abs video-caption">Lorem Ipsum is simply dummy<br>text of the printing and typesetting industry</p>

<div class="abs social">
  <div class="social-item"><i></i><div><small>Share on</small><b>CIRCLENET</b></div></div>
  <div class="social-item"><i></i><div><small>Like us on</small><b>FRIENDWALL</b></div></div>
  <div class="social-item"><i></i><div><small>Follow us on</small><b style="color:#ccc">CHIRPER</b></div></div>
  <div class="social-item"><svg width="16" height="16" viewBox="0 0 16 16"><rect width="16" height="16" rx="2" fill="#f08a2c"/><circle cx="4.5" cy="11.5" r="1.6" fill="#fff"/><path d="M3 7a6 6 0 016 6M3 3.5a9.5 9.5 0 019.5 9.5" stroke="#fff" stroke-width="1.6" fill="none"/></svg><div><small>View us on</small><b>RSS FEED</b></div></div>
  <div class="social-item"><i></i><div><small>Watch our videos on</small><b>REELHUB</b></div></div>
</div>

<div class="abs footer">
  <div class="footer-links">Home | News | Our Services | What we are | What we do | Our Clients | Contact us | Terms Of Use | Privacy Statement | Login</div>
  <div class="footer-copy">Copyright 2013 Brindlow Construction Inc</div>
</div>
</body>
</html>
```